Brightwave MolarNet IT Inc. new website

i need a website for my company which is dedicated to installation and service of computer systems in Dental Offices. I would like for it to encompass a technology feel and professional look. The company deals with all aspects of technology like, Audio Visual, computer systems and networks, Cloud services like data backup, data center. We provide manage services, support and services to Dental Professionals.
Updates

Looking for a Technology font but professional look Added Wednesday, April 20, 2016

Target Market(s)

Dental, Dentist

Industry/Entity Type

Dental

Number of Pages Required

5+ page

Font styles to use
Other font styles liked:
• Futuristic or Techy

Colors
0255a3
ec1f27

Requirements
Must have
• Tabs
Nice to have
• Have no idea maybe some suggestion on your part may help
Should not have
• A professional feel but have a techy look

Files

```html
<!DOCTYPE html>
<html lang="en">
<head>
<meta charset="utf-8">
<title>Brightwave MolarNet IT Inc. – Services</title>
<link href="https://fonts.googleapis.com/css2?family=Exo+2:wght@500;600;700&family=Lato:wght@400;700&display=swap" rel="stylesheet">
<style>
:root{
  --brand:#0255a3;
  --bar:#0d78c4;
  --ink:#1b1b1b;
  --body:#3a3a3a;
  --hero-a:#d7dde4;
  --hero-b:#1d2a44;
  --footer:#363636;
  --footer-deep:#262626;
  --field:#2a2a2a;
  --muted:#d8d8d8;
  --rule:#cfcfcf;
}
*{margin:0;padding:0;box-sizing:border-box}
html,body{width:744px;height:1200px;overflow:hidden;background:#fff}
body{position:relative;font-family:'Lato',sans-serif;color:var(--body)}
.abs{position:absolute}
.topbar{left:0;top:0;width:744px;height:24px;background:var(--bar)}
.topbar .phone{left:490px;top:4px;color:#fff;font:500 12px 'Exo 2',sans-serif;display:flex;align-items:center;gap:6px}
.social{display:flex;gap:6px}
.social span{width:18px;height:18px;border:1.5px solid #fff;border-radius:2px;background:var(--brand)}
.topbar .social{left:598px;top:3px}
.header{left:0;top:24px;width:744px;height:71px;background:#fff}
.brand{left:82px;top:44px;display:flex;align-items:center;gap:7px;font:700 13px 'Exo 2',sans-serif;color:var(--brand);width:170px;line-height:15px}
.brand i{display:block;width:26px;height:26px;background:var(--brand);border-radius:4px;flex:none}
.nav{left:288px;top:52px;display:flex;align-items:center;font:600 9.6px 'Exo 2',sans-serif;color:var(--ink)}
.nav a{color:inherit;text-decoration:none;padding:0 18px;border-left:1px solid #8fb7dc;line-height:11px}
.nav a:first-child{border:0;padding-left:0}
.nav a.active{color:var(--brand)}
.hero{left:0;top:95px;width:744px;height:186px;background:linear-gradient(90deg,var(--hero-a) 0%,#7f8fa5 22%,var(--hero-b) 45%,#17223a 80%,#3a4a66 100%)}
.hero-line{color:#fff;font:600 24px 'Exo 2',sans-serif;white-space:nowrap}
.support-box{left:298px;top:154px;width:418px;height:70px;border:1px solid rgba(255,255,255,.35);background:rgba(255,255,255,.08)}
.support-word{left:314px;top:157px;color:#fff;font:700 48px 'Exo 2',sans-serif;letter-spacing:1px}
.section-title{left:0;width:744px;top:308px;text-align:center;font:700 22px 'Exo 2',sans-serif;color:var(--ink)}
.divider{left:232px;top:351px;width:279px;height:1px;background:var(--rule)}
.divider-mark{left:366px;top:346px;width:12px;height:10px;background:#9a9a9a;border-radius:2px}
.photo{width:140px;height:110px}
.badge{width:60px;height:60px;background:linear-gradient(#1a78cf,var(--brand));border:2px solid #fff;box-shadow:0 1px 4px rgba(0,0,0,.35);display:flex;align-items:center;justify-content:center}
.svc-title{font:600 16px 'Exo 2',sans-serif;color:var(--brand);white-space:nowrap}
.svc-text{width:400px;font-size:9.6px;line-height:16.8px;text-align:justify;color:var(--body)}
.footer{left:0;top:938px;width:744px;height:230px;background:linear-gradient(180deg,#2f2f2f,var(--footer) 40%,#3c3c3c)}
.foot-head{font:600 12px 'Exo 2',sans-serif;color:#fff;padding-bottom:8px;border-bottom:1px dotted #888}
.vsep{width:2px;height:150px;top:998px;background:#2a2a2a;border-right:1px solid #444}
.links{left:83px;top:1003px;list-style:none;font-size:9.6px;color:#fff}
.links li{height:26.3px}
.links li::before{content:"›";margin-right:6px}
.contact{left:210px;color:#fff;font-size:9.6px;display:flex;gap:10px}
.contact svg{flex:none}
.field{left:388px;width:151px;height:18px;background:var(--field);color:#b8b8b8;font-size:8.8px;padding:3px 8px}
.submit{left:388px;top:1124px;width:59px;height:21px;background:var(--brand);color:#fff;font:700 11.5px 'Lato',sans-serif;text-align:center;line-height:21px}
.foot-brand{left:580px;top:1010px;width:92px;text-align:center;font:700 13px 'Exo 2',sans-serif;color:#7a7a7a;line-height:16px}
.foot-brand i{display:block;width:26px;height:26px;margin:0 auto 6px;background:#7a7a7a;border-radius:4px}
.footer .social{left:590px;top:1098px}
.bottombar{left:0;top:1168px;width:744px;height:32px;background:var(--footer-deep);color:#e6e6e6;font-size:9px;text-align:center;line-height:32px}
</style>
</head>
<body>

<div class="abs topbar">
  <div class="abs phone">
    <svg width="14" height="14" viewBox="0 0 14 14"><circle cx="7" cy="7" r="6.2" fill="none" stroke="#fff" stroke-width="1.2"/><path d="M4.6 4.2c.4-.4.8-.3 1 .1l.5 1c.1.3 0 .5-.2.7l-.3.3c.3.8.9 1.4 1.7 1.7l.3-.3c.2-.2.4-.3.7-.2l1 .5c.4.2.5.6.1 1-.6.6-1.4.7-2.2.3-1.3-.6-2.3-1.6-2.9-2.9-.4-.8-.3-1.6.3-2.2z" fill="#fff"/></svg>
    123-555-0142
  </div>
  <div class="abs social" aria-label="Social links"><span></span><span></span><span></span></div>
</div>

<header class="abs header"></header>
<div class="abs brand"><i></i>Brightwave MolarNet IT Inc.</div>
<nav class="abs nav">
  <a href="#" aria-label="Home"><svg width="18" height="14" viewBox="0 0 18 14"><path d="M9 0L0 7.5h2.5V14h4.5V9.5h4V14h4.5V7.5H18z" fill="#1b1b1b"/></svg></a>
  <a href="#">ABOUT US</a>
  <a href="#" class="active">SERVICES</a>
  <a href="#">SUPPORT</a>
  <a href="#">CONTACT US</a>
</nav>

<section class="abs hero" role="img" aria-label="Dental treatment chair beside an IT professional at work"></section>
<div class="abs hero-line" style="left:193px;top:118px">We Provide Manage Services,</div>
<div class="abs support-box"></div>
<div class="abs support-word">SUPPORT</div>
<svg class="abs" style="left:540px;top:163px" width="170" height="52" viewBox="0 0 170 52">
  <g fill="#0c5aa6" stroke="#fff" stroke-width="3">
    <circle cx="26" cy="26" r="23"/><circle cx="84" cy="26" r="23"/><circle cx="142" cy="26" r="23"/>
  </g>
  <rect x="14" y="16" width="24" height="18" rx="3" fill="none" stroke="#fff" stroke-width="2.5"/>
  <path d="M73 21h6l7-6v22l-7-6h-6z" fill="#fff"/>
  <path d="M90 19q4 7 0 14M94 16q6 10 0 20" fill="none" stroke="#fff" stroke-width="2"/>
  <g fill="#fff"><rect x="131" y="15" width="8" height="22"/><rect x="142" y="15" width="12" height="9"/><rect x="142" y="27" width="12" height="10"/></g>
</svg>
<div class="abs hero-line" style="left:316px;top:226px">&amp; Service To Dental Professionals.</div>

<h1 class="abs section-title">Services</h1>
<div class="abs divider"></div>
<div class="abs divider-mark"></div>

<!-- Audio visual -->
<div class="abs photo" style="left:82px;top:374px;background:linear-gradient(135deg,#e8eef4,#7a8a99 50%,#1d2530)" role="img" aria-label="Laptop in a server room"></div>
<div class="abs badge" style="left:190px;top:400px"><svg width="34" height="28" viewBox="0 0 34 28"><path d="M2 9h7l9-8v26l-9-8H2z" fill="#fff"/><path d="M22 8q4 6 0 12M26 4q7 10 0 20" fill="none" stroke="#fff" stroke-width="2.5"/></svg></div>
<h2 class="abs svc-title" style="left:264px;top:375px">Audio Visual Installation &amp; Service</h2>
<p class="abs svc-text" style="left:263px;top:402px">Lorem ipsum dolor sit amet, consectetuer adipiscing elit, sed diam nonummy nibh euismod tincidunt ut laoreet dolore magna aliquam erat volutpat. Ut wisi enim ad minim veniam, quis nostrud exerci tation ullamcorper suscipit lobortis nisl ut aliquip ex ea commodo consequat. Duis autem vel eum iriure dolor in hendrerit in vulputate velit esse molestie consequat, vel illum dolore feugiat nulla facilisis at vero eros et accumsan et iusto odio dignissim qui blandit praesent.</p>

<!-- Networks -->
<h2 class="abs svc-title" style="left:82px;top:514px">Computer Systems And Networks</h2>
<p class="abs svc-text" style="left:82px;top:541px">Lorem ipsum dolor sit amet, consectetuer adipiscing elit, sed diam nonummy nibh euismod tincidunt ut laoreet dolore magna aliquam erat volutpat. Ut wisi enim ad minim veniam, quis nostrud exerci tation ullamcorper suscipit lobortis nisl ut aliquip ex ea commodo consequat. Duis autem vel eum iriure dolor in hendrerit in vulputate velit esse molestie consequat, vel illum dolore feugiat nulla facilisis at vero eros et accumsan et iusto odio dignissim qui blandit praesent.</p>
<div class="abs photo" style="left:523px;top:514px;background:linear-gradient(180deg,#0d1f4d,#3a6bc2 50%,#0a1535)" role="img" aria-label="Rows of networked computer screens under digital data"></div>
<div class="abs badge" style="left:495px;top:539px"><svg width="34" height="32" viewBox="0 0 34 32"><g fill="#fff"><rect x="2" y="2" width="11" height="28"/><rect x="16" y="2" width="16" height="12"/><rect x="16" y="17" width="16" height="13"/></g><g fill="#0255a3"><rect x="5" y="10" width="5" height="3"/><rect x="5" y="18" width="5" height="3"/></g></svg></div>

<!-- Cloud -->
<div class="abs photo" style="left:82px;top:654px;background:linear-gradient(135deg,#0f2a4a,#1f5a8c 55%,#0b1c30)" role="img" aria-label="Hand touching a cloud network diagram"></div>
<div class="abs badge" style="left:190px;top:680px"><svg width="34" height="30" viewBox="0 0 34 30"><path d="M10 12a7 7 0 0 1 13-4 5 5 0 0 1 6 5 4 4 0 0 1-2 7H11a4 4 0 0 1-1-8z" fill="#fff"/><rect x="3" y="18" width="28" height="10" rx="3" fill="#fff" stroke="#0255a3" stroke-width="1.5"/><circle cx="25" cy="23" r="1.8" fill="#0255a3"/></svg></div>
<h2 class="abs svc-title" style="left:264px;top:654px">Cloud Services of Data Backup</h2>
<p class="abs svc-text" style="left:263px;top:681px">Lorem ipsum dolor sit amet, consectetuer adipiscing elit, sed diam nonummy nibh euismod tincidunt ut laoreet dolore magna aliquam erat volutpat. Ut wisi enim ad minim veniam, quis nostrud exerci tation ullamcorper suscipit lobortis nisl ut aliquip ex ea commodo consequat. Duis autem vel eum iriure dolor in hendrerit in vulputate velit esse molestie consequat, vel illum dolore feugiat nulla facilisis at vero eros et accumsan et iusto odio dignissim qui blandit praesent.</p>

<!-- Support -->
<h2 class="abs svc-title" style="left:82px;top:793px">Support Services</h2>
<p class="abs svc-text" style="left:82px;top:820px">Lorem ipsum dolor sit amet, consectetuer adipiscing elit, sed diam nonummy nibh euismod tincidunt ut laoreet dolore magna aliquam erat volutpat. Ut wisi enim ad minim veniam, quis nostrud exerci tation ullamcorper suscipit lobortis nisl ut aliquip ex ea commodo consequat. Duis autem vel eum iriure dolor in hendrerit in vulputate velit esse molestie consequat, vel illum dolore feugiat nulla facilisis at vero eros et accumsan et iusto odio dignissim qui blandit praesent.</p>
<div class="abs photo" style="left:523px;top:793px;height:111px;background:linear-gradient(90deg,#d9b48a,#8a5a32 55%,#3a2414)" role="img" aria-label="Support agent wearing a headset"></div>
<div class="abs badge" style="left:495px;top:818px"><svg width="32" height="32" viewBox="0 0 32 32"><circle cx="16" cy="12" r="7" fill="#fff"/><path d="M4 31c0-8 5-11 12-11s12 3 12 11z" fill="#fff"/><path d="M7 13a9 9 0 0 1 18 0" fill="none" stroke="#fff" stroke-width="2"/><rect x="5" y="11" width="4" height="7" rx="1.5" fill="#fff"/><rect x="23" y="11" width="4" height="7" rx="1.5" fill="#fff"/></svg></div>

<!-- Footer -->
<footer class="abs footer"></footer>
<div class="abs foot-head" style="left:83px;top:966px;width:85px">Quick Links</div>
<div class="abs foot-head" style="left:210px;top:966px;width:129px">Contact Details</div>
<div class="abs foot-head" style="left:390px;top:966px;width:149px">Quick Inquiry</div>
<div class="abs vsep" style="left:189px"></div>
<div class="abs vsep" style="left:368px"></div>
<div class="abs vsep" style="left:561px"></div>

<ul class="abs links">
  <li><b>Home</b></li><li>About Us</li><li>Services</li><li>Support</li><li>Contact Us</li>
</ul>

<div class="abs contact" style="top:1006px">
  <svg width="9" height="12" viewBox="0 0 9 12"><path d="M4.5 0A4.5 4.5 0 0 0 0 4.5C0 8 4.5 12 4.5 12S9 8 9 4.5A4.5 4.5 0 0 0 4.5 0zm0 6.3a1.8 1.8 0 1 1 0-3.6 1.8 1.8 0 0 1 0 3.6z" fill="#fff"/></svg>
  <div style="line-height:12px"><b>Brightwave MolarNet IT Inc.</b><br><span style="display:block;margin-top:3px">2480 Harbor Crest Blvd – Ste 210<br>Lakeview, MN 55901</span></div>
</div>
<div class="abs contact" style="top:1070px;font-size:10.5px">
  <svg width="11" height="11" viewBox="0 0 11 11"><path d="M1.5 1c.5-.5 1-.4 1.3.1l.9 1.5c.2.4.1.7-.2 1l-.5.4c.6 1.3 1.6 2.3 2.9 2.9l.4-.5c.3-.3.6-.4 1-.2l1.5.9c.5.3.6.8.1 1.3-.9.9-2 1-3.1.4C3.9 7.8 2.6 6.5 1.6 4.6 1 3.5 1.1 1.9 1.5 1z" fill="#fff"/></svg>
  123.555.0142
</div>
<div class="abs contact" style="top:1109px">
  <svg width="12" height="9" viewBox="0 0 12 9"><rect x=".5" y=".5" width="11" height="8" fill="none" stroke="#fff"/><path d="M.5.5L6 5l5.5-4.5" fill="none" stroke="#fff"/></svg>
  hello@brightwavemolarnet.com
</div>

<div class="abs field" style="top:1008px">Name</div>
<div class="abs field" style="top:1030px">Email</div>
<div class="abs field" style="top:1051px">Phone</div>
<div class="abs field" style="top:1073px;height:45px">Message</div>
<div class="abs submit">SUBMIT</div>

<div class="abs foot-brand"><i></i>Brightwave MolarNet IT Inc.</div>
<div class="abs social" aria-label="Social links"><span></span><span></span><span></span></div>

<div class="abs bottombar">copyright © 2016 Brightwave MolarNet IT Inc.&nbsp; ALL RIGHT RESERVED</div>

</body>
</html>
```